Virtual assistant company needs letterhead and email signature

We need a letterhead and email signature for our virtual assistant company - taskBeaver (small w capital F). Our tag line is plan ahead | taskBeaver

The colours we would like used are;

#81788c
#dddbe1

For reference our business cards have used #81788c background colour and #dddbe1 text

The fonts we would like used are

Lora
Proxima Nova

Please check out our twitter and facebook for style and feel

Twitter: @taskbeaver
www.examplebook.test/taskbeaver

Please also find attached our landing page and business cards for reference

Any questions please let us know

Thanks
E

Reason: We like the opportunity to receive furthur designs

```html
<!DOCTYPE html>
<html lang="en">
<head>
<meta charset="utf-8">
<title>taskBeaver letterhead</title>
<link rel="stylesheet" href="https://fonts.googleapis.com/css2?family=Lora:wght@400&family=Mulish:wght@400;500&family=Open+Sans:wght@400&display=swap">
<style>
  :root {
    --brand-plum: #716779;
    --brand-mist: #dddbe1;
    --paper: #ffffff;
    --board: #ffffff;
    --board-edge: #e6e6e6;
    --label-ink: #111111;
    --footer-ink: #7b7385;
    --sketch-light: #ececec;
    --sketch-dark: #675e70;
  }
  * { box-sizing: border-box; margin: 0; padding: 0; }
  html, body { width: 1200px; height: 900px; overflow: hidden; background: var(--board); }
  .board {
    position: relative; width: 1200px; height: 900px;
    background: var(--board); border: 1px solid var(--board-edge);
    font-family: "Open Sans", sans-serif;
  }
  .sheet {
    position: absolute; box-shadow: 0 2px 8px rgba(0,0,0,0.18);
    overflow: hidden;
  }
  .sheet--front { left: 175px; top: 37px; width: 462px; height: 653px; background: var(--paper); z-index: 2; }
  .sheet--back  { left: 561px; top: 210px; width: 464px; height: 652px; background: var(--brand-plum); z-index: 1; }

  .letter-header {
    height: 53px; background: var(--brand-plum); color: var(--brand-mist);
    text-align: center; padding-top: 6px;
  }
  .brand-name { font-family: "Lora", serif; font-weight: 400; line-height: 1; }
  .brand-tagline { font-family: "Mulish", sans-serif; font-weight: 500; }
  .letter-header .brand-name { font-size: 25px; }
  .letter-header .brand-tagline { font-size: 9px; margin-top: 2px; }

  .sketch-band { position: absolute; left: 0; width: 100%; }
  .sheet--front .sketch-band {
    bottom: 0; height: 240px;
    background: linear-gradient(to bottom, rgba(236,236,236,0) 0%, var(--sketch-light) 30%, #e4e4e4 100%);
  }
  .sheet--back .sketch-band {
    top: 0; height: 250px;
    background: linear-gradient(to bottom, var(--sketch-dark) 0%, var(--sketch-dark) 55%, rgba(113,103,121,0) 100%);
  }

  .letter-footer {
    position: absolute; left: 0; right: 0; bottom: 13px;
    text-align: center; font-family: "Mulish", sans-serif;
    font-size: 7px; line-height: 10px; color: var(--footer-ink);
  }

  .cover-lockup {
    position: absolute; left: 0; right: 0; top: 350px;
    text-align: center; color: var(--brand-mist);
  }
  .cover-lockup .brand-name { font-size: 46px; }
  .cover-lockup .brand-tagline { font-size: 16px; margin-top: 6px; }

  .view-label { position: absolute; color: var(--label-ink); font-size: 18px; }
  .view-label--front { left: 175px; top: 711px; }
  .view-label--back { left: 983px; top: 178px; }
  .board-title { position: absolute; left: 40px; top: 830px; font-size: 27px; color: var(--label-ink); }
</style>
</head>
<body>
<main class="board">
  <section class="sheet sheet--front" aria-label="Letterhead front">
    <header class="letter-header">
      <div class="brand-name">taskBeaver</div>
      <div class="brand-tagline">plan ahead | taskBeaver</div>
    </header>
    <div class="sketch-band" role="img" aria-label="Faint hand-drawn business sketches of plans, charts and ideas"></div>
    <footer class="letter-footer">
      <p>Lorem ipsum dolor sit amet, consectetur adipiscing elit. Vivamus at eros tempor</p>
      <p>Tel. 00000 000000 &nbsp; Fax: 000000 000000</p>
    </footer>
  </section>

  <section class="sheet sheet--back" aria-label="Letterhead back">
    <div class="sketch-band" role="img" aria-label="Tone-on-tone hand-drawn business sketches of plans, charts and ideas"></div>
    <div class="cover-lockup">
      <div class="brand-name">taskBeaver</div>
      <div class="brand-tagline">plan ahead | taskBeaver</div>
    </div>
  </section>

  <span class="view-label view-label--front">front</span>
  <span class="view-label view-label--back">back</span>
  <h1 class="board-title" style="font-weight:400">letterhead</h1>
</main>
</body>
</html>
```